New modern graphic design for a floor plan flyer for a home builder

Design a flyer/brochure featuring a floor plan. The current design is attached to show what we don't want. Colors can change but need to keep the same logo.

Industry/Entity Type

Graphic Design

```html
<!DOCTYPE html>
<html lang="en">
<head>
<meta charset="utf-8">
<title>The Oak Ridge Plan – Harlan Stone Homes</title>
<link rel="stylesheet" href="https://fonts.googleapis.com/css2?family=Roboto+Condensed:wght@300;400;700&family=Lato:wght@400;700&display=swap">
<style>
  :root {
    --brand-blue: #0f4f97;
    --brand-blue-deep: #0a3f7c;
    --brand-red: #9c1c2b;
    --brand-red-bright: #b0202f;
    --paper: #f3f4f7;
    --paper-light: #fbfbfc;
    --ink: #3b3d42;
    --ink-soft: #55585e;
    --plan-fill: #e6e8ec;
    --white: #ffffff;
  }
  * { margin: 0; padding: 0; box-sizing: border-box; }
  html, body { width: 1029px; height: 1200px; overflow: hidden; }
  body { background: var(--paper); }

  .flyer {
    position: relative;
    width: 1029px;
    height: 1200px;
    overflow: hidden;
    background: linear-gradient(155deg, var(--paper-light) 0%, var(--paper) 55%, #eceef2 100%);
  }
  .flyer__shapes { position: absolute; inset: 0; }

  .brand {
    position: absolute;
    left: 53px;
    top: 70px;
    width: 300px;
    text-align: center;
    color: var(--white);
    font-family: "Roboto Condensed", sans-serif;
    font-weight: 700;
    line-height: 1;
  }
  .brand__mark {
    display: block;
    width: 46px; height: 46px;
    margin: 0 auto 18px;
    border: 5px solid var(--white);
    border-radius: 50%;
  }
  .brand__name { display: block; font-size: 40px; letter-spacing: 1px; }
  .brand__sub { display: block; font-size: 58px; letter-spacing: 2px; margin-top: 4px; }

  .plan-title {
    position: absolute;
    left: 71px;
    top: 518px;
    width: 420px;
    font-family: "Roboto Condensed", sans-serif;
    font-weight: 700;
    text-transform: uppercase;
    white-space: nowrap;
  }
  .plan-title__top {
    display: block;
    color: var(--brand-red);
    font-size: 112px;
    line-height: 96px;
    letter-spacing: -1px;
  }
  .plan-title__bottom {
    display: block;
    color: var(--brand-blue);
    font-size: 86px;
    line-height: 76px;
    letter-spacing: -1px;
    padding-left: 6px;
  }

  .plan-size {
    position: absolute;
    left: 93px;
    top: 706px;
    width: 372px;
    display: flex;
    align-items: center;
    gap: 12px;
    font-family: "Lato", sans-serif;
    font-size: 23px;
    line-height: 28px;
    color: var(--ink);
    white-space: nowrap;
  }
  .plan-size::before, .plan-size::after {
    content: "";
    flex: 1;
    height: 2px;
    background: var(--ink);
  }

  .agent {
    position: absolute;
    left: 83px;
    top: 786px;
    font-family: "Roboto Condensed", sans-serif;
    color: var(--ink);
    white-space: nowrap;
  }
  .agent__label { font-weight: 700; font-size: 28px; line-height: 1.2; }
  .agent__name { font-weight: 300; font-size: 24px; line-height: 1.2; color: var(--ink-soft); }
  .agent__phone {
    display: flex;
    align-items: center;
    gap: 6px;
    margin-top: 10px;
    font-family: "Lato", sans-serif;
    font-weight: 700;
    font-size: 31px;
    line-height: 1.2;
    color: var(--brand-red);
    letter-spacing: 0.5px;
  }
  .agent__phone svg { width: 22px; height: 22px; fill: var(--brand-blue); }

  .floor-plan {
    position: absolute;
    left: 533px;
    top: 374px;
    width: 434px;
    height: 620px;
    background: var(--plan-fill);
    border: 3px solid #8d9097;
  }

  .site-url {
    position: absolute;
    left: 0;
    right: 0;
    top: 1156px;
    padding-left: 77px;
    text-align: center;
    font-family: "Lato", sans-serif;
    font-weight: 700;
    font-size: 20px;
    color: var(--white);
    letter-spacing: 0.5px;
  }
</style>
</head>
<body>
<main class="flyer">
  <svg class="flyer__shapes" viewBox="0 0 1029 1200" width="1029" height="1200" aria-hidden="true">
    <polygon points="0,0 660,0 707,166 0,446" fill="var(--brand-red)"/>
    <polygon points="0,0 530,0 560,136 0,432" fill="var(--white)"/>
    <polygon points="0,0 522,0 552,134 0,426" fill="var(--brand-blue)"/>
    <polygon points="280,0 522,0 552,134 200,320" fill="var(--brand-blue-deep)" opacity="0.55"/>
    <polygon points="0,1162 414,1056 486,1106" fill="var(--brand-blue)"/>
    <polygon points="0,1166 758,1066 1029,1090 1029,1200 0,1200" fill="var(--white)"/>
    <polygon points="0,1172 758,1072 1029,1096 1029,1200 0,1200" fill="var(--brand-red-bright)"/>
  </svg>

  <div class="brand">
    <span class="brand__mark"></span>
    <span class="brand__name">Harlan Stone</span>
    <span class="brand__sub">HOMES</span>
  </div>

  <h1 class="plan-title">
    <span class="plan-title__top">The Oak</span>
    <span class="plan-title__bottom">Ridge Plan</span>
  </h1>

  <p class="plan-size">Sq. Feet: 1996</p>

  <section class="agent">
    <p class="agent__label">Represented By</p>
    <p class="agent__name">Lena Marie Foster, Realtor Brightwater</p>
    <p class="agent__name">Realty Group, Realtors</p>
    <p class="agent__phone">
      <svg viewBox="0 0 24 24"><path d="M6.6 10.8a15.1 15.1 0 0 0 6.6 6.6l2.2-2.2a1 1 0 0 1 1-.25 11.4 11.4 0 0 0 3.6.57 1 1 0 0 1 1 1V20a1 1 0 0 1-1 1A17 17 0 0 1 3 4a1 1 0 0 1 1-1h3.5a1 1 0 0 1 1 1c0 1.25.2 2.45.57 3.57a1 1 0 0 1-.25 1z"/></svg>
      555-014-2297
    </p>
  </section>

  <div class="floor-plan" role="img" aria-label="Floor plan drawing of the home: master suite, patio, dining, living, kitchen, three bedrooms, baths, utility, porch and garage"></div>

  <p class="site-url">www.harlanstonehomes.com</p>
</main>
</body>
</html>
```